Financial Advisory Firm needs a custom content template for financial topics

I need a template that I can reuse often to deliver financial advice commentary on topics ranging from investments to financial planning ideas to tax planning strategies. I am hoping to get a template that is visually exciting and captures readers attention. I will use this template to regularly create new financial and tax content that I will post to social media (e.g. Brivora), my website and targeted email campaigns to current and prospective clients. The content will never be greater than 2 pages.

```html
<!DOCTYPE html>
<html lang="en">
<head>
<meta charset="utf-8">
<title>Ledgerly – Tax Planning Newsletter</title>
<link href="https://fonts.googleapis.com/css2?family=Montserrat:ital,wght@0,300;0,400;0,600;0,700;0,800;1,700&display=swap" rel="stylesheet">
<style>
:root{
  --blue:#0a5fa8;
  --blue-mid:#0b4f8c;
  --navy:#07335d;
  --ink:#333;
  --paper:#fff;
  --backdrop:#e9e6e1;
}
*{box-sizing:border-box;margin:0;padding:0}
html,body{width:1200px;height:821px;overflow:hidden;background:var(--backdrop);font-family:"Montserrat",sans-serif;color:var(--ink)}
.page{position:absolute;top:105px;width:473px;height:611px;background:var(--paper);box-shadow:0 2px 8px rgba(0,0,0,.18)}
.page--one{left:93px}
.page--two{left:632px}
.brand{position:absolute;left:30px;top:28px;display:flex;align-items:center;gap:6px;font-weight:700;font-size:22px;color:var(--blue);letter-spacing:.5px}
.brand__dot{width:12px;height:12px;border-radius:50%;background:var(--blue)}
.issue{position:absolute;left:147px;right:33px;top:27px;border-bottom:1px solid var(--blue);text-align:right;font-size:8.5px;color:var(--blue);padding-bottom:4px}
.title{position:absolute;left:55px;top:114px;width:360px;font-weight:800;font-size:18.5px;line-height:20px;color:var(--blue)}
.section-label{position:absolute;left:55px;font-weight:800;font-size:10.5px;color:var(--blue)}
.facts{position:absolute;left:55px;top:199px;width:364px;list-style:none;background:var(--blue);border:1px solid var(--blue-mid)}
.facts li{color:#fff;font-weight:700;font-size:8.4px;line-height:11.5px;padding:4px 14px 4px 14px;border-top:1px solid rgba(255,255,255,.45)}
.facts li:first-child{border-top:none}
.bullets{list-style:none;font-weight:300;font-size:8.2px;line-height:11.7px;color:var(--ink)}
.bullets li{position:relative;padding-left:14px;margin-bottom:5.5px}
.bullets li::before{content:"";position:absolute;left:1px;top:4px;width:4px;height:4px;border-radius:50%;background:#222}
.thoughts{position:absolute;left:55px;top:381px;width:365px}
.col{position:absolute;top:113px;width:174px}
.col--left{left:55px}
.col--right{left:244px;width:170px}
.col h3{font-weight:800;font-size:9px;color:var(--blue);margin:0 0 7px}
.col .bullets{margin-bottom:9px}
.col .bullets li{margin-bottom:6px}
.quote{position:absolute;left:245px;top:334px;width:203px;height:174px;border-radius:14px;overflow:hidden;background:var(--blue)}
.quote svg{position:absolute;inset:0}
.quote__text{position:absolute;left:18px;top:15px;width:172px;font-weight:700;font-style:italic;font-size:11.2px;line-height:19.2px;color:#fff}
.quote__source{position:absolute;right:38px;bottom:9px;font-weight:700;font-style:italic;font-size:11px;color:#fff}
.footer{position:absolute;left:0;top:557px;width:473px;height:36px}
.footer svg{position:absolute;inset:0}
.contact{position:absolute;top:6px;width:80px;text-align:center;color:#fff;font-size:5.5px;font-weight:400}
.contact svg{position:static;display:block;margin:0 auto 3px}
</style>
</head>
<body>

<section class="page page--one">
  <div class="brand"><span class="brand__dot"></span>Ledgerly</div>
  <div class="issue">APR. 2021, ISSUE 2</div>
  <h1 class="title">2021 INCOME TAX PLANNING FOR THE HARLOW ADMINISTRATION</h1>
  <h2 class="section-label" style="top:181px">WHAT DO WE KNOW?</h2>
  <ul class="facts">
    <li>The Harlow administration has proposed multiple trillions of dollars in additional spending</li>
    <li>Proposed ordinary income tax rate increase for taxpayers with income &gt;$400,000</li>
    <li>Proposed changes to long-term capital gain tax rates for taxpayers with income &gt;$1,000,000. Proposed rates higher than income taxes</li>
    <li>Proposed limit to itemized deductions to 28% of income</li>
    <li>Proposed replacement of Retirement account contribution deduction with a 26% credit.</li>
  </ul>
  <h2 class="section-label" style="top:359px">KEY PLANNING THOUGHTS</h2>
  <ul class="bullets thoughts">
    <li>If there was ever a time to get your financial house in order, now is the time. With multiple proposals for tax increases to potentially at the end of the year. Now is an important time to take action.</li>
    <li>Roth conversions are a strategy to accelerate income, however there are now no options to undo conversions due to the elimination of Roth recharacterizations.</li>
    <li>Opportunities to harvest ordinary income and capital gains should be considered based on your individual situation to act as 'insurance' against tax increases.</li>
    <li>High-income taxpayers with income above the 28% tax bracket who already itemize may benefit from accelerated additional itemized deductions before year-end 2021 as the proposed 28% cap would limit future itemized deductions.</li>
  </ul>
  <footer class="footer">
    <svg width="473" height="36" viewBox="0 0 473 36">
      <rect width="473" height="36" fill="#0a5fa8"/>
      <polygon points="60,0 182,0 170,36 48,36" fill="#0b4f8c"/>
      <polygon points="182,0 304,0 292,36 170,36" fill="#0a4680"/>
      <polygon points="304,0 424,0 412,36 292,36" fill="#07335d"/>
    </svg>
    <div class="contact" style="left:80px"><svg width="12" height="12" viewBox="0 0 12 12"><circle cx="6" cy="6" r="6" fill="#fff"/><path d="M4 3.2l1 1.4-.6.8c.4.9 1 1.5 1.9 1.9l.8-.6 1.4 1-.6 1.1C5.8 8.7 3.3 6.2 3.2 4z" fill="#0a4680"/></svg>555-318-4410</div>
    <div class="contact" style="left:200px"><svg width="12" height="12" viewBox="0 0 12 12"><circle cx="6" cy="6" r="6" fill="#fff"/><rect x="3.5" y="3" width="5" height="6" fill="#0a4680"/><rect x="4.5" y="4" width="3" height="1" fill="#fff"/><rect x="4.5" y="6" width="3" height="2" fill="#fff"/></svg>555-318-4427</div>
    <div class="contact" style="left:321px"><svg width="12" height="12" viewBox="0 0 12 12"><circle cx="6" cy="6" r="6" fill="#fff"/><circle cx="6" cy="6" r="3.8" fill="none" stroke="#07335d" stroke-width=".8"/><ellipse cx="6" cy="6" rx="1.6" ry="3.8" fill="none" stroke="#07335d" stroke-width=".7"/><line x1="2.2" y1="6" x2="9.8" y2="6" stroke="#07335d" stroke-width=".7"/></svg>www.ledgerlyplan.com</div>
  </footer>
</section>

<section class="page page--two">
  <div class="brand"><span class="brand__dot"></span>Ledgerly</div>
  <div class="issue">APR. 2021, ISSUE 2</div>
  <div class="col col--left">
    <h3>Ordinary income</h3>
    <ul class="bullets">
      <li>Proposed top tax bracket of 39.6%, same as before the Tax Cuts &amp; Jobs Act (TCJA)</li>
      <li>Proposed ordinary income tax rate increase for taxpayers with income &gt; $400,000</li>
      <li>Elimination of the Qualified Business Income (QBI) deduction for those making over $400,000/yr</li>
    </ul>
    <h3>Itemized Deductions</h3>
    <ul class="bullets">
      <li>Proposed cap on the limit for deductions. This would limit the maximum benefit to the 28% tax bracket</li>
      <li>The cap would limit the value of itemized deductions. (i.e. if taxpayers were in the 32%, 35% or 39.6% bracket, they would only receive a 28% break on their itemized deductions)</li>
    </ul>
    <h3>Capital Gains</h3>
    <ul class="bullets">
      <li>Proposed change to long-term capital gains rate for taxpayers with income of &gt; $1,000,000. The capital gains rate would move from 20% to 39.6% + 3.8% for the Net Investment Income Tax + state taxes.</li>
    </ul>
  </div>
  <div class="col col--right">
    <ul class="bullets">
      <li>The cap would limit the value of itemized deductions. (i.e. if taxpayers were in the 32%, 35% or 39.6% bracket, they would only receive a 28% break on their itemized deductions)</li>
      <li>Economic Opportunity Zone incentives will still be available and allow deferring capital gains taxes until 2026.</li>
    </ul>
    <h3>Planning</h3>
    <ul class="bullets">
      <li>Higher taxes for the "wealthy" are just around the corner. Work with you CPA and financial planner to set yourself up for financial success.</li>
    </ul>
  </div>
  <figure class="quote">
    <svg width="203" height="174" viewBox="0 0 203 174">
      <rect width="203" height="174" fill="#0a5fa8"/>
      <polygon points="0,0 100,0 60,140 0,140" fill="#0b4f8c"/>
      <polygon points="100,0 203,0 203,80 160,140 60,140" fill="#07335d"/>
      <polygon points="203,80 203,110 192,140 160,140" fill="#0a4680"/>
    </svg>
    <blockquote class="quote__text">“According to tax returns filed through the first 30 weeks of year, 9.6% of filers chose to itemize their deductions on their 2019 tax returns."</blockquote>
    <figcaption class="quote__source">Fiscal Research Council</figcaption>
  </figure>
  <footer class="footer">
    <svg width="473" height="36" viewBox="0 0 473 36">
      <rect width="473" height="36" fill="#0a5fa8"/>
      <polygon points="60,0 182,0 170,36 48,36" fill="#0b4f8c"/>
      <polygon points="182,0 304,0 292,36 170,36" fill="#0a4680"/>
      <polygon points="304,0 424,0 412,36 292,36" fill="#07335d"/>
    </svg>
    <div class="contact" style="left:80px"><svg width="12" height="12" viewBox="0 0 12 12"><circle cx="6" cy="6" r="6" fill="#fff"/><path d="M4 3.2l1 1.4-.6.8c.4.9 1 1.5 1.9 1.9l.8-.6 1.4 1-.6 1.1C5.8 8.7 3.3 6.2 3.2 4z" fill="#0a4680"/></svg>555-318-4410</div>
    <div class="contact" style="left:200px"><svg width="12" height="12" viewBox="0 0 12 12"><circle cx="6" cy="6" r="6" fill="#fff"/><rect x="3.5" y="3" width="5" height="6" fill="#0a4680"/><rect x="4.5" y="4" width="3" height="1" fill="#fff"/><rect x="4.5" y="6" width="3" height="2" fill="#fff"/></svg>555-318-4427</div>
    <div class="contact" style="left:321px"><svg width="12" height="12" viewBox="0 0 12 12"><circle cx="6" cy="6" r="6" fill="#fff"/><circle cx="6" cy="6" r="3.8" fill="none" stroke="#07335d" stroke-width=".8"/><ellipse cx="6" cy="6" rx="1.6" ry="3.8" fill="none" stroke="#07335d" stroke-width=".7"/><line x1="2.2" y1="6" x2="9.8" y2="6" stroke="#07335d" stroke-width=".7"/></svg>www.ledgerlyplan.com</div>
  </footer>
</section>

</body>
</html>
```